Copper Ridge Technologies - Van Wrap

Project Overview
Copper Ridge Technologies is a fast-growing telecommunications company seeking a bold, professional van wrap design for our new fleet vehicle (Ford Transit 250 Cargo). The wrap should clearly communicate our brand identity, highlight our core services, and create strong brand visibility on the road.
Objectives
Design a full vehicle wrap for a Ford Transit 250 Cargo.
Establish instant brand recognition using our logo, brand colors, and clean design.
Communicate our core services in a clear, simple, and modern way.
Ensure the design is legible from a distance and looks professional across a fleet of vehicles.
Brand Identity
Company Name: Copper Ridge Technologies
Industry: Telecommunications / Low Voltage Solutions
Brand Attributes: Professional, Trustworthy, Innovative, Technical Expertise
Brand Colors: Blue, White, Grey (on a full black base)
Logo Files Provided: AI and PSD (attached)
Core Services to Highlight
Cameras
Access Control
Cabling & Networking
Audio / Visual
(We would like these paired with simple, modern icons for quick recognition.)
Van Content:
Should include the following:
Logo (attached)
Services:Cameras
Access Control
Cabling & Networking
Audio / Visual
Phone number: 800-362-5914
Website: www.copperridgenet.example

```html
<!DOCTYPE html>
<html lang="en">
<head>
<meta charset="utf-8">
<title>Copper Ridge Technologies – Van Wrap</title>
<link rel="stylesheet" href="https://fonts.googleapis.com/css2?family=Montserrat:wght@500;600;700&display=swap">
<style>
  :root {
    --wrap-black: #0b0d12;
    --wrap-charcoal: #23272e;
    --brand-blue: #2f8fe6;
    --brand-blue-deep: #1660b8;
    --brand-navy: #0f2d66;
    --brand-grey: #8c9097;
    --brand-white: #ffffff;
    --glass: #3b4048;
    --tyre: #111214;
    --rim: #c7cacf;
    --backdrop: #e9eaec;
  }
  html, body {
    margin: 0;
    width: 1200px;
    height: 1185px;
    overflow: hidden;
    background: var(--backdrop);
  }
  .wrap-sheet { display: block; width: 1200px; height: 1185px; }
  .van-body { fill: var(--wrap-black); }
  .van-glass { fill: var(--glass); }
  .band-blue { fill: var(--brand-blue); }
  .band-grey { fill: var(--brand-grey); opacity: .55; }
  .band-white { fill: var(--brand-white); }
  .band-dash { fill: var(--brand-grey); opacity: .8; }
  .lamp-rear { fill: #c0242b; }
  .lamp-head { fill: #9aa0a8; }
  .tyre { fill: var(--tyre); }
  .rim { fill: var(--rim); }
  .hub { fill: #2a2d32; }
  .brand-name, .brand-sub {
    font-family: "Montserrat", sans-serif;
    font-weight: 600;
    fill: var(--brand-white);
  }
  .brand-name { font-size: 68px; }
  .brand-sub { font-size: 28px; letter-spacing: 11px; }
  .brand-mark { fill: none; stroke: var(--brand-blue); stroke-width: 14; }
  .service {
    font-family: "Montserrat", sans-serif;
    font-weight: 600;
    font-size: 21px;
    fill: var(--brand-white);
  }
  .service-dot { fill: var(--brand-white); }
  .contact {
    font-family: "Montserrat", sans-serif;
    font-weight: 700;
    fill: var(--brand-navy);
  }
  .contact-phone { font-size: 38px; }
  .contact-web { font-size: 29px; }
</style>
</head>
<body>
<svg class="wrap-sheet" viewBox="0 0 1500 1481" xmlns="http://www.w3.org/2000/svg">
  <defs>
    <g id="van-shell">
      <path class="van-body" d="M470 110 L1370 105 Q1405 110 1410 140 L1420 520 Q1420 580 1390 585 L100 595 Q78 590 78 550 L82 495 Q95 420 130 395 L300 320 Q380 200 470 110 Z"/>
      <path class="van-glass" d="M312 330 L420 245 L505 245 L505 385 L320 392 Z"/>
      <path class="band-grey" d="M95 470 L300 440 L1410 390 L1410 430 L330 495 L92 500 Z"/>
      <path class="band-blue" d="M360 500 L1380 400 L1410 450 L1410 470 L380 520 Z"/>
      <path class="band-white" d="M700 500 L1130 430 L1330 470 L1330 485 L1130 450 L760 505 Z"/>
      <path class="band-blue" d="M510 268 L1160 110 L1320 105 L1340 140 L1190 180 L520 285 Z"/>
      <path class="band-grey" d="M480 170 L820 120 L1060 110 L840 150 L500 195 Z"/>
      <path class="band-dash" d="M335 445 L370 435 L395 450 L360 460 Z M385 438 L425 428 L450 442 L410 452 Z M440 430 L480 420 L505 435 L465 445 Z"/>
      <path class="band-dash" d="M690 140 L720 132 L735 142 L705 150 Z M735 130 L765 122 L780 132 L750 140 Z M780 120 L810 113 L825 123 L795 130 Z"/>
      <rect class="lamp-rear" x="1382" y="365" width="24" height="125" rx="4"/>
      <path class="lamp-head" d="M110 425 L170 405 L175 440 L112 455 Z"/>
      <circle class="tyre" cx="265" cy="575" r="78"/>
      <circle class="rim" cx="265" cy="575" r="44"/>
      <circle class="hub" cx="265" cy="575" r="18"/>
      <circle class="tyre" cx="1040" cy="585" r="78"/>
      <circle class="rim" cx="1040" cy="585" r="44"/>
      <circle class="hub" cx="1040" cy="585" r="18"/>
    </g>
  </defs>

  <!-- Driver side: cab facing left -->
  <g class="van van--driver-side">
    <use href="#van-shell"/>
    <circle class="brand-mark" cx="1265" cy="240" r="90"/>
    <g transform="rotate(-11 560 370)">
      <text class="brand-name" x="560" y="370">COPPER RIDGE</text>
      <text class="brand-sub" x="630" y="412">TECHNOLOGIES</text>
    </g>
    <g transform="rotate(-8 580 490)">
      <text class="contact contact-phone" x="580" y="490">800-362-5914</text>
      <text class="contact contact-web" x="895" y="482">copperridgenet.example</text>
    </g>
    <g transform="rotate(-8 600 230)">
      <circle class="service-dot" cx="627" cy="185" r="11"/>
      <text class="service" x="650" y="192">Cameras</text>
      <circle class="service-dot" cx="572" cy="225" r="11"/>
      <text class="service" x="595" y="232">Cabling &amp; Networking</text>
      <circle class="service-dot" cx="880" cy="215" r="11"/>
      <text class="service" x="903" y="222">Audio / Visual</text>
    </g>
  </g>

  <!-- Passenger side: cab facing right -->
  <g class="van van--passenger-side">
    <use href="#van-shell" transform="translate(1500 725) scale(-1 1)"/>
    <circle class="brand-mark" cx="240" cy="960" r="90"/>
    <g transform="rotate(8 375 1015)">
      <text class="brand-name" x="375" y="1015">COPPER RIDGE</text>
      <text class="brand-sub" x="430" y="1057">TECHNOLOGIES</text>
    </g>
    <g transform="rotate(7 345 1115)">
      <text class="contact contact-web" x="345" y="1115">copperridgenet.example</text>
      <text class="contact contact-phone" x="770" y="1118">800-362-5914</text>
    </g>
    <g transform="rotate(6 520 860)">
      <circle class="service-dot" cx="562" cy="845" r="11"/>
      <text class="service" x="585" y="852">Cameras</text>
      <circle class="service-dot" cx="722" cy="845" r="11"/>
      <text class="service" x="745" y="852">Access Control</text>
      <circle class="service-dot" cx="492" cy="882" r="11"/>
      <text class="service" x="515" y="889">Cabling &amp; Networking</text>
      <circle class="service-dot" cx="790" cy="882" r="11"/>
      <text class="service" x="813" y="889">Audio / Visual</text>
    </g>
  </g>
</svg>
</body>
</html>
```